" Minha empresa basicamente funciona da seguinte forma, visito os clientes, pego todas as ideias (Briefing), levo para a empresa, elaboramos o melhor projeto possivel para aquele cliente, apresentamos o projeto, o cliente aprovando, começamos a fabricação. E estamos sempre envolvidos em eventos para trazer tecnologia para nossos clientes. "

```html
<!DOCTYPE html>
<html lang="en">
<head>
<meta charset="utf-8">
<title>Valtorre Letterhead</title>
<link href="https://fonts.googleapis.com/css2?family=Montserrat:wght@400;600;700&family=Open+Sans:wght@400;600&display=swap" rel="stylesheet">
<style>
  :root {
    --canvas: #e6e4e0;
    --paper: #ffffff;
    --gold: #a8844f;
    --ink: #222222;
    --body: #555555;
    --muted: #8a8a8a;
    --faint: #f4efe6;
    --rule: #c9c9c9;
  }
  * { margin: 0; padding: 0; box-sizing: border-box; }
  html, body { width: 1200px; height: 1200px; overflow: hidden; }
  body {
    background: var(--canvas);
    font-family: "Open Sans", sans-serif;
    position: relative;
  }
  .letterhead {
    position: absolute;
    left: 200px; top: 30px;
    width: 800px; height: 1140px;
    background: var(--paper);
    box-shadow: 0 6px 24px rgba(0,0,0,0.12);
    overflow: hidden;
  }
  .watermark-block {
    position: absolute;
    right: 70px; top: 560px;
    width: 300px; height: 460px;
    background: var(--faint);
  }
  .brand {
    position: absolute;
    top: 60px; left: 0; width: 100%;
    text-align: center;
  }
  .brand-mark {
    display: inline-block;
    width: 34px; height: 34px;
    background: var(--gold);
    margin-bottom: 10px;
  }
  .brand-name {
    font-family: "Montserrat", sans-serif;
    font-weight: 600;
    font-size: 26px;
    letter-spacing: 3px;
    color: var(--gold);
  }
  .brand-tagline {
    font-family: "Montserrat", sans-serif;
    font-size: 8px;
    letter-spacing: 3px;
    color: var(--gold);
    margin-top: 3px;
  }
  .heading {
    position: absolute;
    top: 250px; left: 0; width: 100%;
    text-align: center;
  }
  .heading-title {
    font-family: "Montserrat", sans-serif;
    font-weight: 700;
    font-size: 30px;
    letter-spacing: 5px;
    color: var(--ink);
  }
  .heading-subtitle {
    font-family: "Montserrat", sans-serif;
    font-weight: 600;
    font-size: 15px;
    letter-spacing: 4px;
    color: var(--ink);
    margin-top: 6px;
  }
  .heading-rule {
    width: 120px; height: 2px;
    background: var(--ink);
    margin: 16px auto 0;
  }
  .letter-body {
    position: absolute;
    top: 380px; left: 90px; width: 620px;
    position: absolute;
  }
  .letter-body p {
    font-size: 12.5px;
    line-height: 1.75;
    color: var(--body);
    text-align: justify;
    margin-bottom: 18px;
  }
  .sign-off {
    position: absolute;
    top: 790px; right: 90px;
    width: 140px;
    text-align: center;
  }
  .sign-off-label {
    font-size: 12px;
    color: var(--body);
    margin-bottom: 8px;
  }
  .footer-rule {
    position: absolute;
    top: 960px; left: 90px; width: 620px; height: 1px;
    background: var(--rule);
  }
  .contact-list {
    position: absolute;
    top: 985px; left: 90px;
    list-style: none;
  }
  .contact-item {
    display: flex; align-items: center;
    font-size: 12px;
    color: var(--body);
    margin-bottom: 9px;
  }
  .contact-icon {
    width: 18px; height: 18px;
    margin-right: 10px;
    flex: none;
  }
</style>
</head>
<body>
  <main class="letterhead">
    <div class="watermark-block"></div>

    <header class="brand">
      <div class="brand-mark"></div>
      <div class="brand-name">VALTORRE</div>
      <div class="brand-tagline">MÓVEIS PLANEJADOS</div>
    </header>

    <section class="heading">
      <h1 class="heading-title">PAPER MOCKUP</h1>
      <h2 class="heading-subtitle">PSD RESOURCE BY PRINTFORGE</h2>
      <div class="heading-rule"></div>
    </section>

    <section class="letter-body">
      <p>Lorem ipsum dolor sit amet, consectetur adipiscing elit. Donec orci purus, luctus vitae dignissim eu, iaculis sed purus. Vivamus faucibus, ipsum nec aliquet viverra, leo mauris condimentum ligula, sit amet sagittis enim ligula quis arcu. Nam egestas tortor id leo porttitor mattis. In tortor ante, ultricies in suscipit a, tempus non massa. Vivamus et auctor mi. Phasellus nec eros mauris, et scelerisque orci.</p>
      <p>Donec malesuada orci vitae nulla accumsan porta id id massa. Quisque accumsan iaculis magna sit amet fringilla. Maecenas consequat, magna eget tincidunt semper, odio nibh rutrum mi, id feugiat ante nisi eu risus. Vestibulum nunc orci, rhoncus a placerat in, ultricies in eros.</p>
      <p>Sed id augue vitae urna euismod commodo aliquet a quam. Pellentesque ante eros, cursus et malesuada ut, consequat et diam. Nullam erat sem, rhoncus at ullamcorper vitae, rhoncus et leo. Fusce aliquet faucibus ultricies. Morbi semper, est id tincidunt gravida, sem arcu adipiscing quis nibh. Vestibulum id purus lorem.</p>
    </section>

    <div class="sign-off">
      <div class="sign-off-label">Sincerely,</div>
      <svg width="90" height="90" viewBox="0 0 90 90" role="img" aria-label="Handwritten signature over a round company stamp">
        <circle cx="45" cy="45" r="40" fill="none" stroke="#8a8fa3" stroke-width="2"/>
        <circle cx="45" cy="45" r="30" fill="#eef0f4"/>
      </svg>
    </div>

    <div class="footer-rule"></div>

    <ul class="contact-list">
      <li class="contact-item">
        <svg class="contact-icon" viewBox="0 0 18 18"><circle cx="9" cy="9" r="9" fill="#333"/><path d="M6 5l2 0 1 2.5-1.2 1a5 5 0 0 0 2.7 2.7l1-1.2 2.5 1v2a1 1 0 0 1-1 1A8 8 0 0 1 5 6a1 1 0 0 1 1-1z" fill="#fff"/></svg>
        (31) 90000-1234
      </li>
      <li class="contact-item">
        <svg class="contact-icon" viewBox="0 0 18 18"><circle cx="9" cy="9" r="9" fill="#333"/><rect x="6" y="4" width="6" height="10" rx="1" fill="#fff"/><rect x="7" y="5.5" width="4" height="6" fill="#333"/></svg>
        (31) 90000-1235
      </li>
      <li class="contact-item">
        <svg class="contact-icon" viewBox="0 0 18 18"><circle cx="9" cy="9" r="9" fill="#333"/><rect x="4.5" y="5.5" width="9" height="7" fill="#fff"/><path d="M4.5 5.5l4.5 4 4.5-4" fill="none" stroke="#333" stroke-width="1"/></svg>
        contato@valtorre.com.br
      </li>
      <li class="contact-item">
        <svg class="contact-icon" viewBox="0 0 18 18"><circle cx="9" cy="9" r="9" fill="#333"/><circle cx="9" cy="9" r="4.5" fill="none" stroke="#fff" stroke-width="1.2"/><path d="M4.5 9h9M9 4.5v9" stroke="#fff" stroke-width="1"/></svg>
        www.valtorre.com.br
      </li>
    </ul>
  </main>
</body>
</html>
```